Casa Vero Inspections Business Card

I need a business card for my new company. The company is going to provide home inspections. The name of the company is Casa Vero Inspections. I am not sure if I want a single sided card or a double. I have a logo already that I want to incorporate into the card design. I was wondering if I should incorporate a catch phrase on my card or not. If I did the phrase would be "The Intelligent Choice for Home Inspections" but i am unsure how or if to use it on a card. The following information needs to be on the card.
Home Inspection
My Name: Marcus T. Wolford Phone Number: 555-301-7762 Email: mwolford@casaveroinspections.com Website: www.casaveroinspections.com NY HI License # 27300519462

```html
<!DOCTYPE html>
<html lang="en">
<head>
<meta charset="utf-8">
<title>Casa Vero Inspections – Business Card</title>
<link href="https://fonts.googleapis.com/css2?family=Montserrat:wght@500;700&display=swap" rel="stylesheet">
<style>
  :root {
    --backdrop: #c6c7c9;
    --card: #ffffff;
    --brand-blue: #146baa;
    --sky-blue: #74c6ee;
    --white: #ffffff;
  }
  * { margin: 0; padding: 0; box-sizing: border-box; }
  html, body {
    width: 1200px;
    height: 1200px;
    overflow: hidden;
    background: var(--backdrop);
    font-family: "Montserrat", sans-serif;
  }
  body { position: relative; }
  .business-card {
    position: absolute;
    left: 100px;
    top: 313px;
    width: 1000px;
    height: 573px;
    background: var(--card);
    overflow: hidden;
  }
  .brand-name {
    position: absolute;
    left: 0;
    top: 138px;
    width: 436px;
    height: 201px;
    display: flex;
    flex-direction: column;
    align-items: center;
    justify-content: center;
    color: var(--brand-blue);
    font-weight: 700;
    font-size: 44px;
    line-height: 1.15;
    text-align: center;
  }
  .divider {
    position: absolute;
    left: 436px;
    top: 66px;
    width: 3px;
    height: 345px;
    background: var(--sky-blue);
  }
  .person-name {
    position: absolute;
    left: 473px;
    top: 106px;
    width: 500px;
    color: var(--brand-blue);
    font-weight: 700;
    font-size: 41px;
    line-height: 1;
    white-space: nowrap;
  }
  .contact-list {
    position: absolute;
    left: 473px;
    top: 0;
    list-style: none;
    color: var(--brand-blue);
    font-weight: 500;
    font-size: 23px;
  }
  .contact-item {
    position: absolute;
    left: 0;
    display: flex;
    align-items: center;
    white-space: nowrap;
    height: 40px;
  }
  .contact-item.phone { top: 192px; }
  .contact-item.email { top: 245px; }
  .contact-item.web { top: 297px; }
  .contact-item.license { top: 347px; }
  .contact-icon {
    width: 24px;
    height: 24px;
    margin-right: 18px;
    flex: none;
  }
  .tagline-band {
    position: absolute;
    left: 0;
    top: 466px;
    width: 1000px;
    height: 55px;
    background: var(--brand-blue);
    color: var(--white);
    font-weight: 500;
    font-size: 28px;
    display: flex;
    align-items: center;
    justify-content: center;
    letter-spacing: 0.5px;
  }
</style>
</head>
<body>
  <div class="business-card">
    <div class="brand-name">
      <span>Casa Vero</span>
      <span>Inspections</span>
    </div>

    <div class="divider"></div>

    <h1 class="person-name">MARCUS T. WOLFORD</h1>

    <ul class="contact-list">
      <li class="contact-item phone">
        <svg class="contact-icon" viewBox="0 0 24 24" aria-hidden="true">
          <path d="M6.6 2.5c.6 0 1 .3 1.2.8l1.3 3.2c.2.5 0 1-.3 1.4L7.3 9.3c1.2 2.6 3.4 4.8 6 6l1.4-1.5c.4-.4.9-.5 1.4-.3l3.2 1.3c.5.2.8.7.8 1.2v3.3c0 .8-.7 1.5-1.5 1.5C10 20.8 3.2 14 3.2 5.5 3.2 4.7 3.9 4 4.7 4z" fill="var(--sky-blue)"/>
        </svg>
        <span>555-301-7762</span>
      </li>
      <li class="contact-item email">
        <svg class="contact-icon" viewBox="0 0 24 24" aria-hidden="true">
          <rect x="1.5" y="5" width="21" height="14" fill="none" stroke="var(--sky-blue)" stroke-width="2"/>
          <path d="M1.5 5l10.5 8 10.5-8M1.5 19l8-7M22.5 19l-8-7" fill="none" stroke="var(--sky-blue)" stroke-width="1.6"/>
        </svg>
        <span>mwolford@casaveroinspections.com</span>
      </li>
      <li class="contact-item web">
        <svg class="contact-icon" viewBox="0 0 24 24" aria-hidden="true">
          <g fill="none" stroke="var(--sky-blue)" stroke-width="1.8">
            <circle cx="12" cy="12" r="10"/>
            <ellipse cx="12" cy="12" rx="4.5" ry="10"/>
            <path d="M2 12h20M4 7h16M4 17h16"/>
          </g>
        </svg>
        <span>www.casaveroinspections.com</span>
      </li>
      <li class="contact-item license">
        <span>NY HI License # 27300519462</span>
      </li>
    </ul>

    <div class="tagline-band">The Intelligent Choice for Home Inspections</div>
  </div>
</body>
</html>
```